I am looking for help designing my new business cards. I would like rounded edges and a raised logo on the back of the card. I have 2 Logos. One with a boat in it and one without. I'd like the one on the back to be the one that includes the boat and just the name on the front. I have included multiple formats of my logo. Please let me know if you need anymore.

Target Market(s)

Potential buyers and other sales brokers

Industry/Entity Type

Sales - Yacht / Boat Sales

Contact Information for Business Card

Id liike the front to include just the business name portion of the logo along with my name (Corwin Dalby), phone number (555.318.6027), website address (www.dalbymarineco.example) and not my physical address but just "Marlow Harbor, SC". The back should include my full logo that has the boat included. This portion I'd prefer raised amd take up the majority of the space there. Thanks!!

Colors
0054AA
0677BA
7BADD7
CADEEF
E8F1F8
0094D4
00A9DD
6FCCEA
C7EBF8
E9F6FB

Requirements
Must have
• Double sided
Nice to have
• My email address: Corwin@dalbymarineco.example The NMTG logo somewhere small on the front of the card
Should not have
• My full address, prefer only "Marlow Harbor, SC"

```html
<!DOCTYPE html>
<html lang="en">
<head>
<meta charset="utf-8">
<title>Dalby Marine Co – Business Card</title>
<link href="https://fonts.googleapis.com/css2?family=Montserrat:wght@500;800&display=swap" rel="stylesheet">
<style>
  :root {
    --stage: #cbcbcb;
    --paper: #ffffff;
    --navy: #002a62;
    --sea: #0983c0;
    --ink: #141414;
  }
  html, body {
    margin: 0;
    width: 1000px;
    height: 1200px;
    overflow: hidden;
    background: var(--stage);
    font-family: "Montserrat", sans-serif;
  }
  .card {
    position: absolute;
    left: 51px;
    width: 898px;
    height: 538px;
    border-radius: 42px;
    overflow: hidden;
    background: var(--paper);
  }
  .card--front { top: 44px; }
  .card--back { top: 618px; }
  .waves { position: absolute; inset: 0; width: 100%; height: 100%; }
  .wordmark {
    position: absolute;
    margin: 0;
    color: var(--navy);
    font-weight: 800;
    letter-spacing: 1px;
    white-space: nowrap;
  }
  .card--front .wordmark { left: 74px; top: 130px; font-size: 40px; }
  .card--back .wordmark { left: 0; right: 0; top: 302px; text-align: center; font-size: 48px; }
  .contact { position: absolute; left: 509px; top: 282px; }
  .contact__name {
    margin: 0 0 14px;
    font-size: 24px;
    font-weight: 500;
    color: var(--ink);
    letter-spacing: 0.3px;
  }
  .contact__list { list-style: none; margin: 0; padding: 0; }
  .contact__item {
    display: flex;
    align-items: center;
    gap: 14px;
    height: 46px;
    font-size: 23px;
    font-weight: 500;
    color: var(--ink);
    white-space: nowrap;
  }
  .contact__icon { width: 28px; height: 28px; flex: none; }
  .boat-art {
    position: absolute;
    left: 233px;
    top: 80px;
    width: 431px;
    height: 195px;
    border-radius: 8px;
    background: linear-gradient(180deg, #e6eef7 0%, #bcd6ea 60%, #3d93c8 100%);
  }
</style>
</head>
<body>

<section class="card card--front">
  <svg class="waves" viewBox="0 0 898 538" preserveAspectRatio="none" aria-hidden="true">
    <path fill="var(--sea)" d="M0 0H898V65C820 88 720 92 600 68C460 40 330 14 220 24C130 31 60 46 0 64Z"/>
    <path fill="var(--navy)" d="M0 464C70 440 170 436 280 452C420 472 600 520 760 520C820 520 870 500 898 474V538H0Z"/>
  </svg>

  <h1 class="wordmark">DALBY MARINE CO</h1>

  <div class="contact">
    <p class="contact__name">CORWIN DALBY</p>
    <ul class="contact__list">
      <li class="contact__item">
        <svg class="contact__icon" viewBox="0 0 28 28" aria-hidden="true">
          <rect width="28" height="28" rx="4" fill="var(--navy)"/>
          <path fill="#fff" d="M9 7l3 0 1.5 4-2 1.3c.9 2 2.3 3.4 4.2 4.2l1.3-2 4 1.5v3c0 1-1 1.8-2 1.6C12.5 19.8 8.2 15.5 7.4 9c-.2-1 .6-2 1.6-2z"/>
        </svg>
        555.318.6027
      </li>
      <li class="contact__item">
        <svg class="contact__icon" viewBox="0 0 28 28" aria-hidden="true">
          <rect width="28" height="28" rx="4" fill="var(--navy)"/>
          <g fill="none" stroke="#fff" stroke-width="1.4">
            <circle cx="14" cy="14" r="7.5"/>
            <ellipse cx="14" cy="14" rx="3.2" ry="7.5"/>
            <path d="M6.5 14h15M8 10h12M8 18h12"/>
          </g>
        </svg>
        dalbymarineco.example
      </li>
      <li class="contact__item">
        <svg class="contact__icon" viewBox="0 0 28 28" aria-hidden="true">
          <rect width="28" height="28" rx="4" fill="var(--navy)"/>
          <path fill="none" stroke="#fff" stroke-width="1.6" d="M14 21s-5-5.5-5-9a5 5 0 0 1 10 0c0 3.5-5 9-5 9z"/>
          <circle cx="14" cy="12" r="1.8" fill="#fff"/>
          <path stroke="#fff" stroke-width="1.4" d="M9 23h10"/>
        </svg>
        Marlow Harbor, SC
      </li>
    </ul>
  </div>
</section>

<section class="card card--back">
  <svg class="waves" viewBox="0 0 898 538" preserveAspectRatio="none" aria-hidden="true">
    <path fill="var(--sea)" d="M0 0H898V63C840 46 780 20 680 18C540 16 400 52 280 74C200 88 120 92 0 59Z"/>
    <path fill="var(--navy)" d="M0 474C80 500 180 510 300 506C480 498 650 452 760 450C820 450 860 462 898 476V538H0Z"/>
  </svg>

  <div class="boat-art" role="img" aria-label="Illustration of a centre-console sport fishing boat with a T-top cutting through blue waves"></div>

  <h2 class="wordmark">DALBY MARINE CO</h2>
</section>

</body>
</html>
```